We are a bed retailer and require a Banner for my new website which stands out from the crowd.

The banner i require should be bold, Colours dark and light blues and yellow / orange like my logo attached. Also i have attached some ideas of other banners within the website in regqrds to syle im looking for.

The banner should include the following text.
INSTORE ONLY!!
TOP BRANDED, TOP QUALITY BEDS & MATTRESSES ALL SOLD AS ONE OFF, ONE ONLY, GIVEAWAY BARGAINS!
SAVE UPTO 80% OFF R.R.P. DON'T MISS OUT! PRICES WON'T BE BEATEN.

Banner size
width: 2000 pixels
height: 335 pixels.

To look like a high impact sale banner can use red colours

Font styles to use
Sans Serif

Colors
0655a3
ec1f27
33a6d7
ffc214

Requirements
Must have
• High impact like a sale banner!!

```html
<!DOCTYPE html>
<html lang="en">
<head>
<meta charset="utf-8">
<title>Instore Only Sale Banner</title>
<link href="https://fonts.googleapis.com/css2?family=Archivo+Black&family=Archivo:wght@700;800;900&display=swap" rel="stylesheet">
<style>
  :root {
    --sale-red: #ec1f27;
    --deep-red: #c8101a;
    --sun-yellow: #ffc614;
    --ink: #111111;
    --paper: #ffffff;
    --mattress-light: #f1f1f1;
    --mattress-shade: #c9c9c9;
    --mascot-blue: #0655a3;
    --mascot-sky: #33a6d7;
  }
  html, body {
    margin: 0;
    padding: 0;
    width: 1200px;
    height: 1000px;
    overflow: hidden;
    background: var(--paper);
  }
  .canvas {
    position: relative;
    width: 1200px;
    height: 1000px;
  }
  .banner {
    position: absolute;
    left: 0;
    top: 400px;
    width: 1200px;
    height: 200px;
    overflow: hidden;
    font-family: "Archivo", "Helvetica Neue", Arial, sans-serif;
    color: var(--ink);
  }
  .banner-shapes {
    position: absolute;
    inset: 0;
  }
  .mascot {
    position: absolute;
    left: 36px;
    top: 6px;
    width: 140px;
    height: 188px;
    border-radius: 36px 36px 50px 50px;
    background: linear-gradient(160deg, var(--mascot-sky), var(--mascot-blue));
  }
  .mattress-photo {
    position: absolute;
    inset: 0;
  }
  .headline {
    position: absolute;
    left: 220px;
    top: 0;
    width: 730px;
    margin: 0;
    font-family: "Archivo Black", "Arial Black", sans-serif;
    font-size: 84px;
    line-height: 84px;
    letter-spacing: 1px;
    color: var(--sale-red);
    text-shadow: 0 2px 0 var(--deep-red);
    white-space: nowrap;
  }
  .tagline {
    position: absolute;
    left: 222px;
    top: 87px;
    margin: 0;
    font-weight: 800;
    font-size: 12.6px;
    white-space: nowrap;
  }
  .save-label {
    position: absolute;
    left: 250px;
    top: 114px;
    font-weight: 800;
    font-size: 19px;
    line-height: 20px;
  }
  .save-figure {
    position: absolute;
    left: 250px;
    top: 128px;
    font-weight: 900;
    font-size: 58px;
    line-height: 64px;
    letter-spacing: -1px;
  }
  .save-figure sup {
    font-size: 34px;
    vertical-align: 20px;
  }
  .save-off {
    position: absolute;
    left: 345px;
    top: 160px;
    font-weight: 900;
    font-size: 22px;
    line-height: 24px;
  }
  .divider {
    position: absolute;
    left: 542px;
    top: 118px;
    width: 1px;
    height: 68px;
    background: var(--ink);
  }
  .urgency {
    position: absolute;
    left: 570px;
    top: 112px;
    margin: 0;
    font-weight: 900;
    font-size: 43px;
    line-height: 46px;
    white-space: nowrap;
  }
  .urgency-sub {
    position: absolute;
    left: 570px;
    top: 162px;
    margin: 0;
    font-weight: 900;
    font-size: 25.5px;
    line-height: 28px;
    white-space: nowrap;
  }
  .social-tag {
    position: absolute;
    left: 986px;
    top: 160px;
    width: 170px;
    height: 36px;
    background: var(--paper);
    display: flex;
    align-items: center;
    gap: 6px;
    padding-left: 6px;
    box-sizing: border-box;
    font-weight: 800;
    font-size: 13.5px;
  }
  .social-dot {
    width: 24px;
    height: 24px;
    border-radius: 50%;
    background: var(--sun-yellow);
    flex: none;
  }
</style>
</head>
<body>
<div class="canvas">
  <section class="banner">
    <svg class="banner-shapes" width="1200" height="200" viewBox="0 0 1200 200" aria-hidden="true">
      <rect width="1200" height="200" fill="var(--sun-yellow)"/>
      <polygon points="0,0 132,0 12,200 0,200" fill="var(--sale-red)"/>
      <polygon points="994,0 1200,0 1200,200 922,200" fill="var(--sale-red)"/>
      <polygon points="222,115 391,115 385,135 222,135" fill="var(--sale-red)"/>
      <polygon points="222,135 260,135 250,150" fill="var(--deep-red)"/>
      <polygon points="342,160 506,160 498,184 335,184" fill="var(--sale-red)"/>
      <line x1="338" y1="186" x2="372" y2="140" stroke="var(--ink)" stroke-width="2"/>
    </svg>

    <svg class="mattress-photo" width="1200" height="200" viewBox="0 0 1200 200" role="img" aria-label="Photo of stacked white quilted mattresses">
      <defs>
        <linearGradient id="mattressTone" x1="0" y1="0" x2="1" y2="1">
          <stop offset="0" stop-color="var(--mattress-light)"/>
          <stop offset="1" stop-color="var(--mattress-shade)"/>
        </linearGradient>
      </defs>
      <polygon points="1042,0 1200,0 1200,200 968,200" fill="url(#mattressTone)"/>
    </svg>

    <div class="mascot" role="img" aria-label="Store mascot: a cartoon mattress character waving"></div>

    <h1 class="headline">INSTORE ONLY!!</h1>
    <p class="tagline">TOP BRANDED, TOP QUALITY BEDS &amp; MATTRESSES ALL SOLD AS ONE OFF, ONE ONLY, GIVEAWAY BARGAINS!</p>

    <div class="save-label">SAVE UPTO</div>
    <div class="save-figure">80<sup>%</sup></div>
    <div class="save-off">OFF R.R.P.</div>

    <div class="divider"></div>

    <p class="urgency">DON'T MISS OUT!</p>
    <p class="urgency-sub">PRICES WON'T BE BEATEN.</p>

    <div class="social-tag">
      <span class="social-dot"></span>
      <span class="social-handle">@sleepyardbargains</span>
    </div>
  </section>
</div>
</body>
</html>
```